Bookkeeping business needs a digital and print flyer

We need a flyer to promote our virtual bookkeeping services to small and mid-sized businesses in the United States. We want the content and design of the flyer to be consistent with our website: www.brightledgerbookkeeping.example. We would like both a print version and a digital version of the flyer.

```html
<!DOCTYPE html>
<html lang="en">
<head>
<meta charset="utf-8">
<title>Bright Ledger Bookkeeping – Virtual Bookkeeping Flyer</title>
<link href="https://fonts.googleapis.com/css2?family=Montserrat:wght@300;400&family=Poppins:wght@300;400;600;700&display=swap" rel="stylesheet">
<style>
  :root{
    --navy:#0c1f44;
    --navy-deep:#0a1527;
    --ink:#1d2434;
    --yellow:#fbc02d;
    --white:#ffffff;
    --rule:#d9dbe0;
    --passion:#1b2a7a;
  }
  *{margin:0;padding:0;box-sizing:border-box}
  html,body{width:952px;height:1200px;overflow:hidden;background:var(--white)}
  .flyer{position:relative;width:952px;height:1200px;font-family:"Poppins",sans-serif;color:var(--ink)}
  .abs{position:absolute}

  .hero-shape{left:0;top:54px}
  .hero-photo{left:508px;top:89px;width:393px;height:324px;border:1px solid var(--navy);
    background:linear-gradient(135deg,#dfe6ee 0%,#b8c4d2 45%,#6b7b8c 100%)}

  .brand-name{left:70px;top:96px;font-family:"Montserrat",sans-serif;font-weight:300;color:var(--white);
    font-size:30px;line-height:32px;letter-spacing:1px}

  .hero-title{left:61px;top:190px;color:var(--white);white-space:nowrap}
  .hero-title .line-1{font-family:"Montserrat",sans-serif;font-weight:400;font-size:44px;letter-spacing:15px;line-height:50px}
  .hero-title .line-2{font-weight:700;font-size:42px;color:var(--yellow);line-height:42px;margin-top:2px}
  .hero-title .line-3{font-weight:300;font-size:44px;line-height:44px}
  .hero-rule{left:62px;top:339px;width:46px;height:3px;background:var(--yellow)}
  .hero-tagline{left:62px;top:354px;color:var(--white);font-weight:300;font-size:19.5px;line-height:23px;white-space:nowrap}

  .intro{left:62px;top:472px;font-weight:700;font-size:17px;line-height:21px;color:var(--navy);white-space:nowrap}
  .outsource{left:62px;top:564px;width:314px;height:27px;background:var(--yellow);
    font-weight:700;font-size:17px;line-height:27px;color:var(--navy);padding-left:10px}
  .benefits{left:62px;top:612px;list-style:none;white-space:nowrap}
  .benefits li{position:relative;padding-left:20px;font-family:"Montserrat",sans-serif;font-size:15px;line-height:17px;margin-bottom:15px}
  .benefits li svg{position:absolute;left:0;top:3px}
  .office-photo{left:63px;top:902px;width:287px;height:160px;border:2px solid var(--yellow);
    background:linear-gradient(135deg,#cfc7bb 0%,#8a7a66 55%,#3b3a3c 100%)}

  .divider{left:407px;top:457px;width:1px;height:367px;background:var(--rule)}
  .services-title{left:434px;top:457px;font-weight:700;font-size:26px;color:var(--yellow);line-height:30px}
  .services-rule{left:578px;top:472px;width:321px;height:1px;background:var(--navy)}
  .services-banner{left:438px;top:496px;width:406px;height:54px;background:var(--navy);color:var(--white);
    font-family:"Montserrat",sans-serif;font-size:15px;letter-spacing:5px;line-height:21px;padding:6px 0 0 14px;
    box-shadow:0 4px 4px -2px rgba(0,0,0,.35)}
  .service-list{list-style:none;font-family:"Montserrat",sans-serif;font-size:13.5px;line-height:16.5px;white-space:nowrap}
  .service-list li{position:relative;padding-left:20px;margin-bottom:14px}
  .service-list li:last-child{margin-bottom:0}
  .service-list li svg{position:absolute;left:0;top:3px}
  .services-a{left:436px;top:573px}
  .services-b{left:651px;top:575px}

  .person-photo{left:640px;top:800px;width:261px;height:278px;
    background:radial-gradient(ellipse at 55% 45%,#f3efe9 0%,#e3dcd3 45%,#d4d6da 100%)}
  .question-box{left:407px;top:824px;width:326px;height:104px;background:var(--yellow);
    font-family:"Montserrat",sans-serif;font-size:13.5px;line-height:16px;color:var(--navy);padding:11px 0 0 19px;white-space:nowrap}
  .question-box p{margin-bottom:8px}
  .passion{left:417px;top:944px;font-weight:700;font-size:17px;line-height:20px;color:var(--passion)}
  .passion-sub{left:417px;top:995px;font-family:"Montserrat",sans-serif;font-size:13px;line-height:16px;color:var(--ink)}

  .footer{left:0;top:1077px;width:952px;height:123px;background:var(--navy-deep)}
  .cta{left:62px;top:1099px;color:var(--white)}
  .cta .cta-top{font-family:"Montserrat",sans-serif;font-size:21px;letter-spacing:4px;line-height:24px}
  .cta .cta-bottom{font-weight:700;font-size:21px;color:var(--yellow);line-height:24px}
  .contact{color:var(--white);display:flex;align-items:center;gap:10px;font-size:15px;line-height:20px;white-space:nowrap}
  .contact.phone{left:349px;top:1100px;font-weight:700;font-size:16px}
  .contact.address{left:349px;top:1127px;font-family:"Montserrat",sans-serif}
  .contact.email{left:573px;top:1097px;font-family:"Montserrat",sans-serif;font-size:14px}
  .contact.web{left:573px;top:1125px;font-family:"Montserrat",sans-serif;font-size:14px}
</style>
</head>
<body>
<div class="flyer">
  <svg class="abs hero-shape" width="572" height="392" viewBox="0 54 572 392" aria-hidden="true">
    <defs>
      <linearGradient id="heroFill" x1="0" y1="0" x2="1" y2="1">
        <stop offset="0" stop-color="#0c1a33"/>
        <stop offset="0.55" stop-color="#0f2a4d"/>
        <stop offset="1" stop-color="#163a5e"/>
      </linearGradient>
    </defs>
    <polygon points="62,54 508,54 572,89 572,413 508,446 58,446 0,390 0,110" fill="url(#heroFill)"/>
  </svg>
  <div class="abs hero-photo" role="img" aria-label="Photo of a smiling team stacking hands together over a desk in a bright office"></div>

  <div class="abs brand-name">BRIGHT LEDGER<br>BOOKKEEPING</div>

  <div class="abs hero-title">
    <div class="line-1">VIRTUAL</div>
    <div class="line-2">BOOKKEEPING FOR</div>
    <div class="line-3">SMALL BUSINESS</div>
  </div>
  <div class="abs hero-rule"></div>
  <p class="abs hero-tagline">Build Your Business by Focusing on<br>What You Love</p>

  <p class="abs intro">Take charge of your business and<br>concentrate on your strengths to<br>become its hero!</p>
  <div class="abs outsource">Outsource your bookkeeping!</div>
  <ul class="abs benefits">
    <li><svg width="11" height="11" viewBox="0 0 12 12"><circle cx="6" cy="6" r="6" fill="#0c1f44"/><path d="M3.3 6.2l1.8 1.8 3.6-3.8" stroke="#fff" stroke-width="1.6" fill="none"/></svg>Take back your time</li>
    <li><svg width="11" height="11" viewBox="0 0 12 12"><circle cx="6" cy="6" r="6" fill="#0c1f44"/><path d="M3.3 6.2l1.8 1.8 3.6-3.8" stroke="#fff" stroke-width="1.6" fill="none"/></svg>Do more of what you love</li>
    <li><svg width="11" height="11" viewBox="0 0 12 12"><circle cx="6" cy="6" r="6" fill="#0c1f44"/><path d="M3.3 6.2l1.8 1.8 3.6-3.8" stroke="#fff" stroke-width="1.6" fill="none"/></svg>Focus on your strengths and what<br>you do best</li>
    <li><svg width="11" height="11" viewBox="0 0 12 12"><circle cx="6" cy="6" r="6" fill="#0c1f44"/><path d="M3.3 6.2l1.8 1.8 3.6-3.8" stroke="#fff" stroke-width="1.6" fill="none"/></svg>Confidently make business decisions<br>Sail through tax time</li>
    <li><svg width="11" height="11" viewBox="0 0 12 12"><circle cx="6" cy="6" r="6" fill="#0c1f44"/><path d="M3.3 6.2l1.8 1.8 3.6-3.8" stroke="#fff" stroke-width="1.6" fill="none"/></svg>Save over the expense of a full-time<br>employee</li>
    <li><svg width="11" height="11" viewBox="0 0 12 12"><circle cx="6" cy="6" r="6" fill="#0c1f44"/><path d="M3.3 6.2l1.8 1.8 3.6-3.8" stroke="#fff" stroke-width="1.6" fill="none"/></svg>Pay yourself more</li>
    <li><svg width="11" height="11" viewBox="0 0 12 12"><circle cx="6" cy="6" r="6" fill="#0c1f44"/><path d="M3.3 6.2l1.8 1.8 3.6-3.8" stroke="#fff" stroke-width="1.6" fill="none"/></svg>Experience financial peace</li>
  </ul>
  <div class="abs office-photo" role="img" aria-label="Photo of two colleagues reviewing charts on a laptop at a desk with a calculator and notebooks"></div>

  <div class="abs divider"></div>
  <h2 class="abs services-title">SERVICES</h2>
  <div class="abs services-rule"></div>
  <div class="abs services-banner">BOOKKEEPING TAILORED TO<br>YOUR BUSINESS NEEDS</div>

  <ul class="abs service-list services-a">
    <li><svg width="10" height="10" viewBox="0 0 12 12"><circle cx="6" cy="6" r="6" fill="#fbc02d"/><path d="M3.3 6.2l1.8 1.8 3.6-3.8" stroke="#fff" stroke-width="1.6" fill="none"/></svg>Catch-up and clean-up<br>services</li>
    <li><svg width="10" height="10" viewBox="0 0 12 12"><circle cx="6" cy="6" r="6" fill="#fbc02d"/><path d="M3.3 6.2l1.8 1.8 3.6-3.8" stroke="#fff" stroke-width="1.6" fill="none"/></svg>Transaction importation and<br>categorization</li>
    <li><svg width="10" height="10" viewBox="0 0 12 12"><circle cx="6" cy="6" r="6" fill="#fbc02d"/><path d="M3.3 6.2l1.8 1.8 3.6-3.8" stroke="#fff" stroke-width="1.6" fill="none"/></svg>Monthly reconciliation of all<br>accounts, including assets<br>and loans.</li>
    <li><svg width="10" height="10" viewBox="0 0 12 12"><circle cx="6" cy="6" r="6" fill="#fbc02d"/><path d="M3.3 6.2l1.8 1.8 3.6-3.8" stroke="#fff" stroke-width="1.6" fill="none"/></svg>Monthly financial reports<br>(Balance Sheet, Income<br>Statement, Cash Flow)</li>
  </ul>
  <ul class="abs service-list services-b">
    <li><svg width="10" height="10" viewBox="0 0 12 12"><circle cx="6" cy="6" r="6" fill="#fbc02d"/><path d="M3.3 6.2l1.8 1.8 3.6-3.8" stroke="#fff" stroke-width="1.6" fill="none"/></svg>Monthly video conference<br>Annual tax-prep package<br>sent to your preparer</li>
    <li><svg width="10" height="10" viewBox="0 0 12 12"><circle cx="6" cy="6" r="6" fill="#fbc02d"/><path d="M3.3 6.2l1.8 1.8 3.6-3.8" stroke="#fff" stroke-width="1.6" fill="none"/></svg>A/R &amp; A/P</li>
    <li><svg width="10" height="10" viewBox="0 0 12 12"><circle cx="6" cy="6" r="6" fill="#fbc02d"/><path d="M3.3 6.2l1.8 1.8 3.6-3.8" stroke="#fff" stroke-width="1.6" fill="none"/></svg>Payroll coordination<br>1099s</li>
    <li><svg width="10" height="10" viewBox="0 0 12 12"><circle cx="6" cy="6" r="6" fill="#fbc02d"/><path d="M3.3 6.2l1.8 1.8 3.6-3.8" stroke="#fff" stroke-width="1.6" fill="none"/></svg>Bill pay and receipt<br>management</li>
    <li><svg width="10" height="10" viewBox="0 0 12 12"><circle cx="6" cy="6" r="6" fill="#fbc02d"/><path d="M3.3 6.2l1.8 1.8 3.6-3.8" stroke="#fff" stroke-width="1.6" fill="none"/></svg>Budgeting</li>
  </ul>

  <div class="abs person-photo" role="img" aria-label="Photo of a confident businessman in a white shirt and tie with arms crossed, framed by grey sunburst rays"></div>
  <div class="abs question-box">
    <p>Did you get into business because<br>you loved recording finances?</p>
    <p>Reconciling bank statements?</p>
    <p>Prepping for taxes?</p>
  </div>
  <p class="abs passion">YOU WANT TO FOLLOW<br>YOUR PASSION,</p>
  <p class="abs passion-sub">DO WHAT&nbsp; YOU DO BEST TO<br>BUILD A BOOMING BUSINESS.</p>

  <footer class="abs footer"></footer>
  <div class="abs cta">
    <div class="cta-top">REQUEST YOUR</div>
    <div class="cta-bottom">FREE CONSULTATION</div>
  </div>
  <div class="abs contact phone">
    <svg width="12" height="12" viewBox="0 0 12 12"><circle cx="6" cy="6" r="6" fill="#fbc02d"/><path d="M4 3.2c-.6.3-.8 1-.4 1.8.6 1.3 1.7 2.4 3 3 .8.4 1.5.2 1.8-.4l-1-.9-.7.5c-.7-.3-1.3-.9-1.6-1.6l.5-.7z" fill="#0a1527"/></svg>
    555-014-2867
  </div>
  <div class="abs contact address">
    <svg width="12" height="14" viewBox="0 0 12 14"><path d="M6 0a5 5 0 0 0-5 5c0 3.6 5 9 5 9s5-5.4 5-9a5 5 0 0 0-5-5z" fill="#fbc02d"/><circle cx="6" cy="5" r="2" fill="#0a1527"/></svg>
    Lorem Ipsum,ipsum
  </div>
  <div class="abs contact email">
    <svg width="14" height="14" viewBox="0 0 14 14"><circle cx="7" cy="7" r="7" fill="#fbc02d"/><rect x="3.5" y="4.5" width="7" height="5" fill="none" stroke="#0a1527" stroke-width="1"/><path d="M3.5 4.5l3.5 3 3.5-3" fill="none" stroke="#0a1527" stroke-width="1"/></svg>
    hello@brightledgerbookkeeping.example
  </div>
  <div class="abs contact web">
    <svg width="14" height="14" viewBox="0 0 14 14"><circle cx="7" cy="7" r="7" fill="#fbc02d"/><circle cx="7" cy="7" r="4" fill="none" stroke="#0a1527" stroke-width="1"/><ellipse cx="7" cy="7" rx="1.8" ry="4" fill="none" stroke="#0a1527" stroke-width="1"/><path d="M3 7h8" stroke="#0a1527" stroke-width="1"/></svg>
    www.brightledgerbookkeeping.example
  </div>
</div>
</body>
</html>
```